'Cradle Ahead' promotional brochure

We have designed a 6 week program to educate impending first-time parents about the things they need to know to survive the first 6 months. Sessions delivered by general practitioner/family doctor, dietician, physiotherapist, speech pathologist and psychologist. Our promotional blurb is: 'A comprehensive education program for first-time parents-to-be, delivered over 6 weeks by health professionals in your community, about everything you need to know to look after your baby (and yourself!) in the first 6 months'. I now want to put together a promotional brochure to be distributed to those couples who express an interest which will provide further details of what will be delivered in the course.
Updates
In terms of layout, I envisaged a double sided A4 size, foldable into 3 sections, but very happy to be guided on this.
Target Market(s)
To appeal to a young, well educated demographic. First time parents couples.
Industry/Entity Type
Medical
Font styles to use
Other font styles liked:
- Playfair Display
Requirements
Must have
- Playfair display font to be consistent with our logo (attached). Logo also included please. Some consistency with colours of logo please.
Nice to have
- I am a doctor, and have no creative genes! But prefer a clean and professional appearance overall. Not too cluttered in overall appearance.
Should not have
- No cheesy pictures of babies.

```html
<!DOCTYPE html>
<html lang="en">
<head>
<meta charset="utf-8">
<title>Cradle Ahead – Program Outline</title>
<link rel="stylesheet" href="https://fonts.googleapis.com/css2?family=Playfair+Display:ital,wght@0,700;1,700;1,800&display=swap">
<style>
  :root {
    --ink: #111111;
    --green: #8cc63f;
    --green-deep: #9acd3c;
    --paper: #ffffff;
  }
  * { margin: 0; padding: 0; box-sizing: border-box; }
  html, body { width: 1200px; height: 848px; overflow: hidden; }
  body {
    background: linear-gradient(to bottom, var(--paper) 0%, var(--paper) 68%, #e3f2c8 80%, var(--green-deep) 100%);
    font-family: 'Playfair Display', Georgia, serif;
    font-weight: 700;
    color: var(--ink);
    font-size: 14.4px;
    letter-spacing: 1.9px;
    line-height: 27.2px;
  }
  .panel {
    position: absolute;
    top: 19px;
    width: 372px;
  }
  .panel--left { left: 15px; }
  .panel--middle { left: 419px; }
  .panel--right { left: 812px; width: 372px; }
  .week-tag {
    display: inline-block;
    background: var(--green);
    color: var(--paper);
    font-style: italic;
    font-weight: 800;
    font-size: 18px;
    letter-spacing: 1px;
    line-height: 24px;
    padding: 0 12px 0 5px;
    border-radius: 0 12px 12px 0;
    margin-bottom: 2px;
  }
  .week + .week { margin-top: 24px; }
  p { text-align: justify; hyphens: auto; padding-left: 4px; }
  p + p { margin-top: 27px; }
  .topics { list-style: none; padding-left: 4px; }
  .topics li::before { content: "▪ "; }
  .topics--indented { padding-left: 38px; }
  .topics--indented li::before { content: "▪"; }
  .topics--top { padding-left: 30px; margin-bottom: 26px; margin-top: -4px; }
  .topics--top li::before { content: "▪"; }
</style>
</head>
<body>
  <section class="panel panel--left">
    <div class="week">
      <span class="week-tag">Week 1</span>
      <p>GP Dr Helen Marsh will share information for Mum’s own health after delivery. Topics include:</p>
      <ul class="topics">
        <li>Vaccinations in pregnancy</li>
        <li>Bleeding, bladder and bowel after delivery</li>
        <li>Breastfeeding, engorgement and mastitis</li>
        <li>Bottle feeding</li>
        <li>Post-natal anxiety &amp; depression</li>
        <li>Intimacy and contraception</li>
      </ul>
    </div>
    <div class="week">
      <span class="week-tag">Week 2</span>
      <p>Session 1 – Clinical Psychologist Dr. Nadia Rowe will discuss changes in relationships as couples becomes parents, gender roles in parenting and post-natal depression.</p>
      <p>Session 2 – Physiotherapist Tessa Harlow will present advice for Mums regarding exercise during and after pregnancy, looking after the pelvic floor during and after pregnancy, and abdominal muscle separation management. She will also provide advice for promoting babies’ neck strength and minimising the risk of flat spots on the head and encouraging gross motor skills in the first 6 months.</p>
    </div>
  </section>

  <section class="panel panel--middle">
    <div class="week">
      <span class="week-tag">Week 3</span>
      <p>Session 1 – Dietician Amy Calder provides advice for Mums regarding healthy eating during pregnancy and lactation, normal weight gain during pregnancy and realistic weight loss after. She will also discuss the evidence regarding breastfeeding VS bottle-feeding, normal infant weight gain and introducing solids (including those with potential for allergy).</p>
      <p>Session 2 – Paediatric Speech Pathologist Claire Benton will share information about latching and breast-feeding troubles &amp; tongue tie, advice about dummies and finger-sucking, introducing solids &amp; feeding (including ‘pouch’ food), encouraging language development and current evidence about electronic devices impacting language development.</p>
    </div>
    <div class="week">
      <span class="week-tag">Week 4</span>
      <p>GP Dr Helen Marsh will share advice about your babies’ health in the first 6 months, including:</p>
      <ul class="topics topics--indented">
        <li>Skin of newborns</li>
        <li>Sleeping</li>
        <li>Crying</li>
        <li>Immunisations</li>
        <li>Fever and infections</li>
      </ul>
    </div>
  </section>

  <section class="panel panel--right">
    <ul class="topics topics--top">
      <li>Diarrhoea and constipation</li>
      <li>Teething</li>
      <li>Understanding a baby’s signals</li>
    </ul>
    <div class="week">
      <span class="week-tag">Week 5</span>
      <p>Session 1 – Clinical Psychologist Dr Nadia Rowe will share information about bonding &amp; attachment with your baby, how to promote their social &amp; emotional development and how to manage separation anxiety. She will also discuss positive parenting approaches.</p>
    </div>
    <div class="week">
      <span class="week-tag">Week 6</span>
      <p>Session 1 – Secret Men’s Business – a men-only session (including beer!) with a new father for frank discussion about the road ahead. Mums will do a shopping excursion with the GP &amp; Dietician to FreshMart to look at baby products and food – the good and the bad!</p>
      <p>Session 2 - Program review, reflection and evaluation and future session planning when baby is 6 months of age.</p>
    </div>
  </section>
</body>
</html>
```